New Business Card Design Project

I would like to purchase a customized version of a design you have previously submitted - https://www.plorvexa.com/design/7314826<br/><br/>I would like to incorporate the attached Images for my fitness company "TrelmoKor Athletics". My initial services is personal training and athletic performance. I would like a card that has one a shiny black side with the silver logo and the side with a white background utilizing the gold logo. On the white side, put "Sports Performance and Functional Strength Training" under the logo.
Industry/Entity Type
Fitness
Contact Information for Business Card
Quillan Morrow
Owner and Trainer
555.271.9384
quillan.morrow@trelmokorathletics.com
Look and feel
Each slider illustrates characteristics of the customer's brand and the style your logo design should communicate.

```html
<!DOCTYPE html>
<html lang="en">
<head>
<meta charset="utf-8">
<title>TrelmoKor Athletics – Business Card</title>
<link href="https://fonts.googleapis.com/css2?family=Roboto:wght@400;500&display=swap" rel="stylesheet">
<style>
  :root {
    --stage: #3a3a3a;
    --card-black: #1c1c1c;
    --card-white: #ffffff;
    --gold: #a88a4e;
    --silver: #cfcfcf;
    --ink-dark: #2a2a2a;
    --text-light: #ffffff;
  }
  * { box-sizing: border-box; margin: 0; padding: 0; }
  html, body { width: 1200px; height: 900px; overflow: hidden; }
  body {
    background: var(--stage);
    font-family: "Roboto", Arial, sans-serif;
    display: flex;
    flex-direction: column;
    align-items: center;
    justify-content: center;
    gap: 40px;
  }
  .card {
    position: relative;
    width: 700px;
    height: 400px;
    border-radius: 22px;
    overflow: hidden;
    box-shadow: 0 10px 30px rgba(0,0,0,0.45);
  }
  .card--back { background: var(--card-black); }
  .card--front { background: var(--card-white); }
  .card__wave { position: absolute; inset: 0; }

  .brand {
    position: absolute;
    display: flex;
    align-items: center;
    gap: 14px;
    font-weight: 500;
    letter-spacing: 0.12em;
    text-transform: uppercase;
    white-space: nowrap;
  }
  .brand__dot {
    width: 44px; height: 44px;
    border-radius: 50%;
    flex: none;
  }
  .card--back .brand {
    left: 50%; top: 50%;
    transform: translate(-50%, -50%);
    color: var(--silver);
    font-size: 26px;
  }
  .card--back .brand__dot { background: var(--silver); }
  .card--front .brand {
    left: 44px; top: 50px;
    color: var(--ink-dark);
    font-size: 24px;
  }
  .card--front .brand__dot { background: var(--ink-dark); }

  .tagline {
    position: absolute;
    left: 44px;
    top: 112px;
    color: var(--ink-dark);
    font-size: 14px;
    letter-spacing: 0.04em;
    white-space: nowrap;
  }

  .contact {
    position: absolute;
    right: 42px;
    top: 252px;
    text-align: right;
    color: var(--text-light);
  }
  .contact__name {
    color: var(--gold);
    font-size: 30px;
    font-weight: 400;
    letter-spacing: 0.04em;
    text-transform: uppercase;
    white-space: nowrap;
  }
  .contact__role { font-size: 16px; margin-top: 2px; }
  .contact__rule {
    width: 34px; height: 2px;
    background: var(--gold);
    margin: 10px 0 8px auto;
  }
  .contact__line {
    display: flex;
    justify-content: flex-end;
    align-items: center;
    gap: 10px;
    font-size: 15px;
    line-height: 1.55;
    white-space: nowrap;
  }
  .contact__icon { width: 14px; height: 14px; flex: none; }
</style>
</head>
<body>

  <section class="card card--back" aria-label="Card back">
    <div class="brand"><span class="brand__dot"></span>TrelmoKor Athletics</div>
  </section>

  <section class="card card--front" aria-label="Card front">
    <svg class="card__wave" viewBox="0 0 700 400" preserveAspectRatio="none" aria-hidden="true">
      <path d="M0,200 C30,250 90,262 240,262 C420,262 570,200 700,236 L700,400 L0,400 Z" fill="var(--card-black)"/>
      <path d="M40,180 C50,230 110,246 250,246 C420,246 580,190 700,222" fill="none" stroke="var(--gold)" stroke-width="9"/>
    </svg>

    <div class="brand"><span class="brand__dot"></span>TrelmoKor Athletics</div>
    <div class="tagline">Sports Performance and Functional Strength Training</div>

    <div class="contact">
      <div class="contact__name">Quillan Morrow</div>
      <div class="contact__role">Owner and Trainer</div>
      <div class="contact__rule"></div>
      <div class="contact__line">555.271.9384
        <svg class="contact__icon" viewBox="0 0 24 24" aria-hidden="true"><path fill="var(--gold)" d="M6.6 10.8a15.1 15.1 0 0 0 6.6 6.6l2.2-2.2c.3-.3.7-.4 1-.2 1.1.4 2.3.6 3.6.6.6 0 1 .4 1 1V20c0 .6-.4 1-1 1A17 17 0 0 1 3 4c0-.6.4-1 1-1h3.5c.6 0 1 .4 1 1 0 1.3.2 2.5.6 3.6.1.3 0 .7-.2 1z"/></svg>
      </div>
      <div class="contact__line">quillan.morrow@trelmokorathletics.com
        <svg class="contact__icon" viewBox="0 0 24 24" aria-hidden="true"><rect x="2.5" y="5" width="19" height="14" rx="1.5" fill="none" stroke="var(--gold)" stroke-width="2"/><path d="M3 6l9 7 9-7" fill="none" stroke="var(--gold)" stroke-width="2"/></svg>
      </div>
    </div>
  </section>

</body>
</html>
```